Design for 3.31” x 84” vinyl banner for tradeshow

Hello, I am looking for a design that will be printed on a 33.31” x 84” vinyl banner for my company’s tradeshow booth.

-Design

My vision: I want to give you the full background, because I think it’ll help. We design insulation for electronic tools that go in high temperature oilwells. Interestingly, a lot of the electronic tools that go down these oil wells are also used in geothermal wells. However the electronics would melt in these high temperature geothermal wells if they were not insulated. A lot of companies that make tools for the oil market are trying to re-purpose their existing tools for the geothermal market…..and to do this, they would need our insulation.

So, our sign needs to conveys this message: Trying to enter the geothermal logging market? it's as simple as increasing the temp. rating for your existing tools

This sign will be placed at our company’s booth at an industry tradeshow. The sign needs to have a similar style to our existing signs. I’ve included images of our booth and all of our other signs. This sign doesn’t have to be identical in artistic style, but be fairly similar.

-Art Requirements:

At least 1 Image of RBT logo

I’ve included several different variations. Use your judgement to select the one that you think is most fitting.

Do not use the portion of the logo that says “40 years”. Feel free to crop that out if you would like.

At least 2 images of logging tools. You can select more than 2 if you think that’s necessary. Logging tools are the long metal tubes.

I’ve included several pictures of different logging tools. I would like to see at least 2 pictures of tools on the banner. Please include the image titled “Full, double centarlizer” It could look cool if this picture extended the full length of the banner (just a suggestion). I purchased these images off of picvaultly.For the second image of the tool, feel free to include whatever tool you think looks best.

-Colors and font: Like I mentioned above, I would like it to look close to the other signs we have at our booth. Please select colors and fonts that will fit with our other signs.

-Other thoughts/suggestions

When most people in our industry think of geothermal, the automatically associate it with extremely high temperatures. I’m open to seeing warmer colors (orange/red) that help convey this idea.

I’m also open to seeing pictures of geothermal power plants, I included an image of this titled “geothermal” that you may use if you like. This is not mandatory, just a suggestion.

-Text: the main text needs to be: “Trying to enter the Geothermal logging market? Ask us about increasing the temperature rating for your existing tools” No other text is required.

Printing/Art specifications:

I’ll be giving the design I receive off art-huddle to a local banner printing shop. I’ve included their printing and art guidelines, please take a look at it and let me know if you have any questions. It’s pretty detailed so I hope it provides you with enough information. The design would have to follow the requirements in the two attached word documents.

Target Market(s)

oil and gas professionals

Industry/Entity Type

oil and gas/geothermal

Font styles to use
Other font styles liked:
• Fonts similar the font used on our other tradeshow signs (images attached)

Colors
F0912C
F2A743
F7CA91
FBE8D2
FDF5EE

Requirements
Must have
• -At least 1 Image of RBT logo, At least 2 images of logging tools (1 of these 2 pictures must be image titled "full double centralizer", he main text needs to be: “Trying to enter the Geothermal logging market? Ask us about increasing the temperature rating for your existing tools” , the design must follow the requirements in the printing and art guideline documents I attached.
Nice to have
• please select colors and fonts that will fit with our other signs.

```html
<!DOCTYPE html>
<html lang="en">
<head>
<meta charset="utf-8">
<title>RBT Geothermal Tradeshow Banner</title>
<link rel="stylesheet" href="https://fonts.googleapis.com/css2?family=Anton&display=swap">
<style>
  :root {
    --backdrop: #b5b5b5;
    --banner-white: #ffffff;
    --ink: #000000;
    --tool-dark: #5a5656;
    --tool-mid: #8a8585;
    --tool-copper: #b0683a;
  }
  html, body {
    margin: 0;
    padding: 0;
    width: 1200px;
    height: 1200px;
    overflow: hidden;
    background: var(--backdrop);
  }
  .canvas {
    position: relative;
    width: 1200px;
    height: 1200px;
    background: var(--backdrop);
  }
  .banner {
    position: absolute;
    left: 169px;
    top: 112px;
    width: 383px;
    height: 965px;
    background: var(--banner-white);
    overflow: hidden;
    font-family: "Anton", "Oswald", sans-serif;
    color: var(--ink);
  }
  .brand {
    position: absolute;
    left: 99px;
    top: 36px;
    display: flex;
    align-items: center;
    gap: 8px;
  }
  .brand-mark {
    width: 52px;
    height: 52px;
    background: var(--ink);
    border-radius: 4px;
  }
  .brand-name {
    font-size: 17px;
    line-height: 1.15;
    letter-spacing: 0.3px;
    text-transform: uppercase;
  }
  .headline, .message { margin: 0; font-weight: 400; }
  .line {
    position: absolute;
    white-space: nowrap;
    line-height: 1;
    text-transform: uppercase;
  }
  .headline .lead { left: 18px; top: 238px; font-size: 29px; }
  .headline .big  { font-size: 44px; }
  .headline .geo  { left: 22px; top: 282px; }
  .headline .log  { left: 71px; top: 338px; }
  .headline .mkt  { left: 39px; top: 396px; }
  .message .line { font-size: 22px; }
  .message .l1 { left: 194px; top: 584px; }
  .message .l2 { left: 176px; top: 620px; }
  .message .l3 { left: 154px; top: 656px; }
  .message .l4 { left: 130px; top: 692px; }
  .message .l5 { left: 110px; top: 728px; }
  .tool {
    position: absolute;
    transform-origin: center center;
    border-radius: 3px;
  }
  .tool-long {
    left: calc(190px - 340px);
    top: calc(558px - 4px);
    width: 680px;
    height: 8px;
    transform: rotate(-62.1deg);
    background: linear-gradient(90deg, var(--tool-copper) 0%, var(--tool-dark) 6%, var(--tool-mid) 50%, var(--tool-dark) 94%, var(--tool-copper) 100%);
  }
  .tool-short {
    left: calc(101px - 79px);
    top: calc(598px - 6px);
    width: 158px;
    height: 12px;
    transform: rotate(-71.6deg);
    background: linear-gradient(90deg, var(--tool-dark) 0%, var(--tool-mid) 55%, var(--tool-dark) 100%);
  }
</style>
</head>
<body>
  <div class="canvas">
    <section class="banner">
      <div class="brand">
        <span class="brand-mark"></span>
        <span class="brand-name">Redbank<br>Thermal, Inc.</span>
      </div>

      <div class="tool tool-long" role="img" aria-label="Photo of a full-length logging tool with double centralizer"></div>
      <div class="tool tool-short" role="img" aria-label="Photo of a shorter logging tool with centralizer"></div>

      <h1 class="headline">
        <span class="line lead">Trying to enter the</span>
        <span class="line big geo">Geothermal</span>
        <span class="line big log">Logging</span>
        <span class="line big mkt">Market?</span>
      </h1>

      <p class="message">
        <span class="line l1">Ask us</span>
        <span class="line l2">About&nbsp; increasing</span>
        <span class="line l3">The temperature</span>
        <span class="line l4">Rating for your</span>
        <span class="line l5">Existing tools</span>
      </p>
    </section>
  </div>
</body>
</html>
```